An international wholesale business needs letterhead design

Logo file is attached. Please design a letterhead with the following details:

- Company Name and Logo
- Address
- VAT Registration number
- Phone No
- Website address

```html
<!DOCTYPE html>
<html lang="en">
<head>
<meta charset="utf-8">
<title>Korvel Trading Letterhead</title>
<link href="https://fonts.googleapis.com/css2?family=Open+Sans:wght@400;600;700&display=swap" rel="stylesheet">
<style>
  :root {
    --backdrop: #b4b5b7;
    --paper: #ffffff;
    --brand-red: #c1272f;
    --brand-grey: #8a9197;
    --ink: #333333;
    --ink-soft: #444444;
    --signature-tone: #e6e6e6;
  }
  * { margin: 0; padding: 0; box-sizing: border-box; }
  html, body {
    width: 1200px; height: 900px; overflow: hidden;
    background: var(--backdrop);
    font-family: "Open Sans", Arial, sans-serif;
  }
  .letterhead {
    position: absolute; left: 275px; top: 29px;
    width: 650px; height: 842px;
    background: var(--paper);
    color: var(--ink);
  }
  .side-band-red {
    position: absolute; left: 0; top: 0; width: 29px; height: 721px;
    background: var(--brand-red);
  }
  .side-band-grey {
    position: absolute; left: 0; top: 724px; width: 29px; bottom: 0;
    background: var(--brand-grey);
  }
  .brand {
    position: absolute; right: 69px; top: 52px;
    display: flex; align-items: center; gap: 10px;
  }
  .brand-dot {
    width: 34px; height: 34px; border-radius: 50%;
    background: var(--brand-red);
  }
  .brand-name {
    font-size: 30px; font-weight: 700; color: var(--brand-red);
    letter-spacing: 0.5px; line-height: 1;
  }
  .letter {
    position: absolute; left: 72px; right: 69px; top: 0;
    font-size: 11.6px; letter-spacing: 0.3px; color: var(--ink);
  }
  .letter-date, .letter-salutation, .letter-closing, .letter-sender {
    position: absolute; left: 0; font-weight: 600; font-size: 12px; letter-spacing: 0.6px;
  }
  .letter-date { top: 166px; }
  .letter-salutation { top: 196px; }
  .letter-body {
    position: absolute; left: 0; right: 0; top: 227px;
    line-height: 15.3px; text-align: justify;
  }
  .letter-body p + p { margin-top: 15.3px; }
  .letter-closing { top: 553px; }
  .signature {
    position: absolute; left: -4px; top: 578px; width: 244px; height: 50px;
    background: linear-gradient(90deg, var(--signature-tone), #f3f3f3);
    border-radius: 4px;
  }
  .letter-sender { top: 645px; }
  .contact {
    position: absolute; right: 69px; top: 737px;
    text-align: right; font-size: 11px; letter-spacing: 0.6px; color: var(--ink-soft);
    line-height: 15px;
  }
  .contact-line { display: flex; justify-content: flex-end; align-items: center; gap: 4px; }
  .contact-phone { margin-top: 7px; }
  .contact svg { width: 9px; height: 9px; }
  .vat {
    position: absolute; right: 69px; top: 816px;
    font-size: 8.5px; font-weight: 700; letter-spacing: 0.6px; color: var(--brand-red);
  }
</style>
</head>
<body>
  <main class="letterhead">
    <div class="side-band-red"></div>
    <div class="side-band-grey"></div>

    <header class="brand">
      <span class="brand-dot"></span>
      <span class="brand-name">KORVEL TRADING</span>
    </header>

    <section class="letter">
      <div class="letter-date">Monday, January 05, 2020</div>
      <div class="letter-salutation">Dear Madam/Sir</div>
      <div class="letter-body">
        <p>Lorem ipsum dolor sit amet, consectetur adipiscing elit, sed do eiusmod tempor incididunt ut labore et dolore magna aliqua. Ut enim ad minim veniam, quis nostrud exercitation ullamco laboris nisi ut aliquip ex ea commodo consequat. Duis aute irure dolor in reprehenderit in voluptate velit esse cillum dolore eu fugiat nulla pariatur. Excepteur sint occaecat cupidatat non proident, sunt in culpa qui officia deserunt mollit anim id est laborum.</p>
        <p>Curabitur pretium tincidunt lacus. Nulla gravida orci a odio. Nullam varius, turpis et commodo pharetra, est eros bibendum elit, nec luctus magna felis sollicitudin mauris. Integer in mauris eu nibh euismod gravida. Duis ac tellus et risus vulputate vehicula. Donec lobortis risus a elit. Etiam tempor. Ut ullamcorper, ligula eu tempor congue, eros est euismod turpis, id tincidunt sapien risus a quam. Maecenas fermentum consequat mi. Donec fermentum. Pellentesque malesuada nulla a mi. Duis sapien sem, aliquet nec, commodo eget, consequat quis, neque. Aliquam faucibus, elit ut dictum aliquet, felis nisl adipiscing sapien, sed malesuada diam lacus eget erat. Cras mollis scelerisque nunc. Nullam arcu. Aliquam consequat. Curabitur augue lorem, dapibus quis, laoreet et, pretium ac, nisi. Aenean magna nisl, mollis quis, molestie eu, feugiat in, orci. In hac habitasse platea dictumst.</p>
      </div>
      <div class="letter-closing">Sincerely,</div>
      <div class="signature" role="img" aria-label="Handwritten signature of Tamsin Revell"></div>
      <div class="letter-sender">Ms. Tamsin Revell</div>
    </section>

    <footer>
      <div class="contact">
        <div class="contact-line">2750 Harwick Lane Suite 400</div>
        <div class="contact-line">Brookfield, OH 4412</div>
        <div class="contact-line contact-phone">555-218-0473
          <svg viewBox="0 0 24 24" aria-hidden="true"><path fill="#c1272f" d="M6.6 10.8a15.1 15.1 0 0 0 6.6 6.6l2.2-2.2a1 1 0 0 1 1-.25 11.4 11.4 0 0 0 3.6.57 1 1 0 0 1 1 1V20a1 1 0 0 1-1 1A17 17 0 0 1 3 4a1 1 0 0 1 1-1h3.5a1 1 0 0 1 1 1c0 1.25.2 2.45.57 3.6a1 1 0 0 1-.25 1z"/></svg>
        </div>
        <div class="contact-line">www.korveltrading.com
          <svg viewBox="0 0 24 24" aria-hidden="true"><g fill="none" stroke="#c1272f" stroke-width="2.4"><circle cx="12" cy="12" r="10"/><path d="M2 12h20M12 2c3 3 3 17 0 20M12 2c-3 3-3 17 0 20"/></g></svg>
        </div>
      </div>
      <div class="vat">VAT REGISTRATION NUMBER</div>
    </footer>
  </main>
</body>
</html>
```